Homepage design

Hi
I m workingon hosting my website tallowbrook.net on wordpress but the new design for the homepage is not good
I need a design just for that page on how to organise things and what to put there

```html
<!DOCTYPE html>
<html lang="en">
<head>
<meta charset="utf-8">
<title>Tallowbrook – Currency Exchange</title>
<link href="https://fonts.googleapis.com/css2?family=Roboto:wght@400;500;700&family=Ubuntu:wght@400;500&display=swap" rel="stylesheet">
<style>
:root{
  --navy:#173a6a;
  --navy-dark:#12305a;
  --red:#d5252b;
  --link:#1f6cb5;
  --sand:#9a7c64;
  --brown:#6e3a27;
  --sky:#1f8ad5;
  --green:#5dbb2e;
  --text:#2b2b2b;
  --line:#1f4f8a;
}
*{box-sizing:border-box;margin:0;padding:0}
html,body{width:720px;height:1200px;overflow:hidden;background:#fff}
body{position:relative;font-family:"Roboto",Arial,sans-serif;color:var(--text)}
.abs{position:absolute}
a{color:inherit;text-decoration:none}

/* header */
.brand{left:76px;top:16px;display:flex;align-items:center;gap:8px}
.brand-dot{width:18px;height:18px;border-radius:50%;background:var(--red)}
.brand-name{font-weight:700;font-size:20px;color:var(--navy)}
.phone{left:348px;top:8px;font-size:11px;font-weight:500;color:var(--navy);display:flex;align-items:center;gap:5px}
.open-top{left:518px;top:7px;text-align:right;color:var(--red);line-height:1}
.open-top b{display:block;font-size:11.5px;font-weight:500}
.open-top small{font-size:7.5px;font-weight:700}
.toplinks{right:80px;top:46px;font-size:8.5px;font-weight:500;color:var(--link)}
.mainnav{left:78px;top:66px;font-size:11.5px;font-weight:500;color:var(--navy);letter-spacing:.2px;white-space:nowrap}
.mainnav .on{color:var(--red)}

/* hero */
.hero{left:72px;top:86px;width:576px;height:199px;border:1px solid var(--line);background:linear-gradient(90deg,#d8cfc3 0%,#c9cfc8 45%,#bcc6c2 100%);overflow:hidden}
.hero-photo{position:absolute;left:0;top:0;width:240px;height:100%;background:radial-gradient(ellipse at 45% 45%,#f0d9bf 0%,#d8b995 35%,#9f8a75 70%,#c3c3bb 100%)}
.hero-copy{position:absolute;left:237px;top:24px;font-family:"Ubuntu",sans-serif;font-size:24px;line-height:34px;color:#1b4a7b}
.hero-copy em{font-style:normal;font-weight:500;color:#2aa4e0}
.dots{position:absolute;right:13px;bottom:9px;display:flex;gap:3px}
.dots i{width:8px;height:8px;border-radius:50%;background:var(--navy-dark)}
.dots i:first-child{background:#2d8fd8}

/* panels */
.panel{background:var(--navy);border:1px solid #0e2748;color:#fff}
.panel h2{font-size:14.5px;font-weight:500;line-height:15px}
.panel p{font-size:8.1px;line-height:12.7px}
.rule{border-top:1px dotted #cfd8e4}
.more{font-size:8px;font-weight:700;display:inline-flex;align-items:center;gap:4px}
.more::after{content:"";border-left:5px solid #fff;border-top:3.5px solid transparent;border-bottom:3.5px solid transparent}

.intro{left:72px;top:294px;width:381px;height:252px;padding:7px 8px}
.intro p{margin-top:7px}
.intro .rule{position:absolute;left:8px;right:8px;top:218px}
.intro .more{position:absolute;left:8px;top:224px}

.quote{left:462px;top:294px;width:186px;height:252px;background:var(--sand);border:1px solid #7c624f;padding:10px 6px;color:#fff}
.quote h3{font-size:14px;font-weight:400;text-decoration:underline;margin-left:1px}
.frow{display:flex;align-items:center;justify-content:space-between;height:14px;margin-top:16px;font-size:7.8px;white-space:nowrap}
.frow span:last-child{width:116px;height:14px;background:#fff}
.frow .captcha{width:67px;margin-right:49px;background:linear-gradient(90deg,#e9eef6,#c9d4e6)}
.quote-btn{position:absolute;right:7px;bottom:13px;background:#6e3422;border:1px solid #4b2114;font-size:9px;padding:3px 6px;display:flex;align-items:center;gap:4px}

.personal{left:72px;top:555px;width:186px;height:171px;padding:7px 8px}
.business{left:267px;top:555px;width:186px;height:171px;padding:7px 8px}
.personal p,.business p{margin-top:9px}
.personal .rule,.business .rule{position:absolute;left:8px;right:8px;top:136px}
.links2{position:absolute;left:8px;right:8px;top:142px;display:flex;justify-content:space-between}

.open-box{left:462px;top:555px;width:186px;height:46px;background:var(--brown);border:1px solid #4c2216;color:#fff;padding:8px 9px;line-height:1}
.open-box b{display:block;font-size:14px;font-weight:500}
.open-box small{display:block;font-size:10px;font-weight:500;margin-left:22px;margin-top:1px}
.open-box svg{position:absolute;right:8px;top:10px}

.safety{left:462px;top:612px;width:186px;height:114px;background:var(--navy);border:1px solid #0e2748;color:#fff}
.safety .stripe{position:absolute;left:0;top:0;width:19px;height:100%;background:#1f8ad5}
.safety h3{position:absolute;left:29px;right:0;top:7px;text-align:center;font-size:14px;font-weight:500}
.safety .rule{position:absolute;left:29px;right:9px;top:28px}
.safety ul{position:absolute;left:38px;top:42px;list-style:none;font-size:8px;font-weight:500}
.safety li{display:flex;align-items:center;gap:5px;height:19px}
.lock{position:absolute;left:7px;top:49px}

/* app bar */
.apps{left:72px;top:735px;width:576px;height:71px;border:1px solid var(--line);background:#fff}
.phone-img{position:absolute;left:9px;top:2px;width:30px;height:64px;border-radius:3px;background:linear-gradient(180deg,#3a3a3a,#7f8ea3 40%,#222)}
.dl{position:absolute;left:60px;top:17px;color:var(--navy)}
.dl b{display:block;font-size:15px;font-weight:500}
.dl span{font-size:10px;font-weight:500}
.store{position:absolute;top:14px;display:flex;align-items:center;gap:6px;font-size:15px;font-weight:500;color:var(--navy)}
.store i{width:44px;height:44px;border-radius:50%;background:var(--navy)}

/* news & video */
.news{left:72px;top:816px;width:381px;height:155px;background:var(--sky);border:1px solid #1670b0;color:#fff;padding:6px 9px}
.news h2{font-size:14.5px;font-weight:500}
.news dl{margin-top:6px}
.news dt{font-size:7px;font-weight:700;margin-top:6px}
.news dd{font-size:6.8px;margin-top:5px}
.news .rule{position:absolute;left:9px;right:9px;top:121px}
.news .more{position:absolute;left:9px;top:126px}

.video{left:462px;top:816px;width:186px;height:128px;background:#000;color:#fff;padding:6px 8px}
.video h2{font-size:14.5px;font-weight:500}
.video .cap{font-size:7px;margin-top:5px}
.video-shot{position:absolute;left:2px;top:48px;width:182px;height:64px;background:linear-gradient(180deg,#2b3240 0%,#6a4a3a 40%,#d38a3b 65%,#2a2a30 100%)}
.play{position:absolute;left:82px;top:22px;width:20px;height:20px;border-radius:3px;background:rgba(0,0,0,.7)}
.play::after{content:"";position:absolute;left:7px;top:5px;border-left:8px solid #fff;border-top:5px solid transparent;border-bottom:5px solid transparent}
.vbar{position:absolute;left:2px;right:2px;bottom:2px;height:12px;background:#222;font-size:6px;padding:3px 0 0 52px;color:#ddd}
.socials{left:470px;top:955px;display:flex;gap:14px}
.socials i{width:16px;height:16px;border-radius:2px}

/* footer */
.cols{left:76px;top:984px;display:flex}
.col{width:114px;height:116px;border-left:1px solid var(--line);padding-left:6px;font-size:7.6px;color:var(--navy)}
.col h4{font-size:8px;font-weight:700;margin-bottom:5px}
.col li{list-style:none;line-height:14.4px}
.col li.tall{line-height:9px;padding-top:2px}
.foot-links{left:0;width:720px;top:1114px;text-align:center;font-size:8.5px;font-weight:500;color:var(--navy)}
.badge{left:82px;top:1136px;width:46px;height:24px;background:#8b2332}
.legal{left:0;width:720px;top:1133px;text-align:center;font-size:8px;line-height:14.6px;color:var(--navy)}
</style>
</head>
<body>

<header>
  <div class="abs brand"><span class="brand-dot"></span><span class="brand-name">Tallowbrook</span></div>
  <div class="abs phone">
    <svg width="8" height="10" viewBox="0 0 8 10"><path d="M1.5 0.5l2 0.5-0.8 2.2 -1 .5c.4 1.6 1.2 2.8 2.4 3.7l1-.6 1.8 1.4-1 1.7C2.6 9.3.5 6.2.5 2z" fill="#173a6a"/></svg>
    +44 (0)20 5550 1847
  </div>
  <div class="abs open-top"><b>OPEN AN ACCOUNT</b><small>Authorised by the FSB</small></div>
  <nav class="abs toplinks">HOME &nbsp;|&nbsp; LOGIN &nbsp;|&nbsp; CONTACT US</nav>
  <nav class="abs mainnav"><span class="on">HOME</span> &nbsp;|&nbsp; PERSONAL &nbsp;|&nbsp; BUSINESS &nbsp;|&nbsp; MARKET KNOWLEDGE &nbsp;|&nbsp; CURRENCY TOOLS &nbsp;|&nbsp; WHY TALLOWBROOK</nav>
</header>

<section class="abs hero">
  <div class="hero-photo" role="img" aria-label="Photo of a smiling business advisor in a dark suit"></div>
  <div class="hero-copy">
    <div><em>Free</em> registration</div>
    <div><em>Secure</em> transaction</div>
    <div><em>Competitive</em> exchange rates</div>
  </div>
  <div class="dots"><i></i><i></i><i></i><i></i></div>
</section>

<section class="abs panel intro">
  <h2>Currency Exchange and International Payments</h2>
  <p>At Tallowbrook we are a foreign currency broker for private and business clients.</p>
  <p>We place our business focus on providing our clients with the most competitive rates for currency exchange and money transfers whilst executing the highest quality of client service. Strategically located in London's financial district, we have immediate access to critical market insight enabling our clients to make a quick and informed decision as to when to convert currency.</p>
  <p>Our FX specialists buy and sell currency at rates close to interbank value. We monitor the currency market, work with live rates and aim to get the best rate at the time for our clients. Dealing with a large amount of international payments brings economies of scale which allows us to achieve even better exchange rates.</p>
  <p>As piece of mind for our clients is critical to our business, we operate to strict guidelines. Our principle bank is Hartwell Bank in which our clients funds are held in secure segregated client accounts.</p>
  <div class="rule"></div>
  <a class="more">KNOW MORE</a>
</section>

<section class="abs quote">
  <h3>Request a Currency Quote</h3>
  <div class="frow"><span>Full Name*</span><span></span></div>
  <div class="frow"><span>Company</span><span></span></div>
  <div class="frow"><span>Telephone*</span><span></span></div>
  <div class="frow"><span>E-mail*</span><span></span></div>
  <div class="frow"><span>Captcha Code</span><span class="captcha" role="img" aria-label="Captcha image"></span></div>
  <div class="frow"><span>Image Text*</span><span></span></div>
  <a class="quote-btn">Get a Quote
    <svg width="6" height="9" viewBox="0 0 6 9"><path d="M1 1l3.5 3.5L1 8" stroke="#fff" stroke-width="1.4" fill="none"/></svg></a>
</section>

<section class="abs panel personal">
  <h2>Personal Currency<br>Exchange</h2>
  <p>Whether you are buying or selling overseas property or simply undertaking money transfers abroad, you need to buy the relevant foreign currency and optimise your budget. This is where we can help and offer competitive rates for both currency exchange</p>
  <div class="rule"></div>
  <div class="links2"><a class="more">KNOW MORE</a><a class="more">HOW IT WORKS</a></div>
</section>

<section class="abs panel business">
  <h2>Business Currency<br>Exchange</h2>
  <p>We help you to minimise your foreign exchange risks on profit and optimise your international payment costs. Use Tallowbrook's expertise to spend less time managing your international payments and devote more time to growing your</p>
  <div class="rule"></div>
  <div class="links2"><a class="more">KNOW MORE</a><a class="more">HOW IT WORKS</a></div>
</section>

<section class="abs open-box">
  <b>OPEN AN ACCOUNT</b><small>Authorised by the FSB</small>
  <svg width="18" height="22" viewBox="0 0 18 22"><circle cx="8" cy="13" r="6.5" stroke="#fff" stroke-width="2" fill="none"/><path d="M9 12L15 3" stroke="#fff" stroke-width="2"/></svg>
</section>

<section class="abs safety">
  <div class="stripe"></div>
  <svg class="lock" width="26" height="34" viewBox="0 0 26 34"><path d="M6 15V9a7 7 0 0114 0v2" stroke="#fff" stroke-width="3" fill="none"/><rect x="1" y="15" width="24" height="18" fill="#fff"/><path d="M8 24l4 4 7-8" stroke="#173a6a" stroke-width="2.4" fill="none"/></svg>
  <h3>YOUR SAFETY</h3>
  <div class="rule"></div>
  <ul>
    <li><svg width="13" height="11" viewBox="0 0 13 11"><path d="M1 6l4 4 7-9" stroke="#5dbb2e" stroke-width="2.5" fill="none"/></svg>Authorised by the FSB</li>
    <li><svg width="13" height="11" viewBox="0 0 13 11"><path d="M1 6l4 4 7-9" stroke="#5dbb2e" stroke-width="2.5" fill="none"/></svg>Your funds held at Hartwell Bank</li>
    <li><svg width="13" height="11" viewBox="0 0 13 11"><path d="M1 6l4 4 7-9" stroke="#5dbb2e" stroke-width="2.5" fill="none"/></svg>Secure segregated accounts</li>
  </ul>
</section>

<section class="abs apps">
  <div class="phone-img" role="img" aria-label="Smartphone showing the mobile app"></div>
  <div class="dl"><b>DOWNLOAD</b><span>Tallowbrook Mobile Application</span></div>
  <div class="store" style="left:269px"><i></i>Phone App</div>
  <div class="store" style="left:429px"><i></i>Tablet App</div>
</section>

<section class="abs news">
  <h2>Currency News</h2>
  <dl>
    <dt>International Currency Exchange News 1st February to 8th February 2013:</dt>
    <dd>* Global markets report: Call us on +44 (0)20 5550 1847 or email us to info@tallowbrook.net...</dd>
    <dt>International Currency Exchange News 1st February to 8th February 2013:</dt>
    <dd>* Global markets report: Call us on +44 (0)20 5550 1847 or email us to info@tallowbrook.net...</dd>
    <dt>International Currency Exchange News 1st February to 8th February 2013:</dt>
    <dd>* Global markets report: Call us on +44 (0)20 5550 1847 or email us to info@tallowbrook.net...</dd>
  </dl>
  <div class="rule"></div>
  <a class="more">SIGN UP FOR DAILY RATES UPDATE</a>
</section>

<section class="abs video">
  <h2>Introduction Video</h2>
  <div class="cap">Tallowbrook - Who we are</div>
  <div class="video-shot" role="img" aria-label="Video still of a city skyline at sunset"><span class="play"></span></div>
  <div class="vbar">0:00 / 1:24</div>
</section>
<div class="abs socials">
  <i style="background:#3b5a98"></i><i style="background:#3a3a3a"></i><i style="background:#3f8fcf"></i><i style="background:#f07a1a"></i><i style="background:#1f77b3"></i><i style="background:#c4302b"></i>
</div>

<footer>
  <div class="abs cols">
    <div class="col"><h4>Services</h4><ul><li>Open an individual account</li><li>Open a business account</li><li>Other services</li><li>Refer a friend</li><li>Affiliates</li></ul></div>
    <div class="col"><h4>Exchange</h4><ul><li>Canadian dollars to US dollars</li><li>Dollar to euros</li><li>Dollar to pound</li><li>Euros to dollars</li><li>Euros to pounds</li><li>Pounds to dollars</li><li>Pounds to euros</li></ul></div>
    <div class="col"><h4>Foreign Exchange</h4><ul><li>Best euro rate</li><li>Best exchange rates</li><li>Currency exchange</li><li>Currency news</li></ul></div>
    <div class="col"><h4>Currency Tools</h4><ul><li>Calculator exchange rate</li><li>Currency converter</li><li>Currency conversion</li><li class="tall">Foreign currency exchange rates</li></ul></div>
    <div class="col"><h4>Why Tallowbrook</h4><ul><li>About us</li><li>Regulatory</li><li>Careers</li><li>Contact us</li></ul></div>
  </div>
  <nav class="abs foot-links">HOME &nbsp;|&nbsp; SIGN UP &nbsp;|&nbsp; LOGIN &nbsp;|&nbsp; CONTACT US</nav>
  <div class="abs badge"></div>
  <div class="abs legal">
    <div>Tallowbrook Ltd. Registered in England Number 8140275-Registered Office: 14 Orchard Lane London E2 7QT.</div>
    <div><b>FSB Authorisation Number:</b> 604127. <b>Revenue Office Money Laundering Regulation Number:</b> 13580294.</div>
    <div>Copyright © Tallowbrook 2012 Regulatory info</div>
    <div>Disclaimer &amp; Privacy | Site Map</div>
  </div>
</footer>

</body>
</html>
```